Brisbane IT support business needs our first website

Hi All,

We are after a new website design for our IT solutions and support business.The business name is Harlow Digital Systems Group, or HDSG for short. We provide a range of solutions and services within the IT space.

I would like to utilize the two colours in our business logo I have uploaded.

I understand this is initially for the design only aspect of the site, but I would like to engage the winner to finish coding the website and finalize after also.

Target Market(s)

Other businesses owners and home users.

Industry/Entity Type

Business

Requirements
Must have
• Nice clean and functional design utilizing our business colours from the logo.

```html
<!DOCTYPE html>
<html lang="en">
<head>
<meta charset="utf-8">
<title>HDSG — Harlow Digital Systems Group</title>
<link href="https://fonts.googleapis.com/css2?family=Open+Sans:ital,wght@0,300;0,400;0,600;0,700;1,400;1,600&display=swap" rel="stylesheet">
<style>
  :root {
    --orange: #e8772a;
    --navy: #0e4a66;
    --teal: #17718f;
    --teal-deep: #0a3a52;
    --ink: #333333;
    --muted: #777777;
    --dark: #2d2d2d;
    --darker: #1f1f1f;
    --footer: #2b2b2b;
    --mist: #e7e7e7;
    --white: #ffffff;
  }
  * { box-sizing: border-box; margin: 0; padding: 0; }
  html, body { width: 1200px; height: 2281px; overflow: hidden; }
  body { font-family: "Open Sans", Arial, sans-serif; color: var(--ink); background: var(--white); position: relative; }
  section, header, footer { position: absolute; left: 0; width: 1200px; }

  /* Header */
  .site-header { top: 0; height: 126px; background: var(--white); }
  .brand { position: absolute; left: 236px; top: 24px; display: flex; align-items: center; gap: 14px; color: var(--navy); font-weight: 700; }
  .brand-dot { width: 90px; height: 90px; border-radius: 50%; background: var(--navy); }
  .brand-name { font-size: 44px; line-height: 1; letter-spacing: 1px; }
  .brand-full { font-size: 10px; line-height: 1.2; margin-top: 4px; text-transform: uppercase; width: 150px; }
  .contact-bar { position: absolute; right: 236px; top: 32px; display: flex; align-items: center; gap: 10px; font-size: 16px; color: var(--ink); }
  .contact-bar .sep { width: 1px; height: 12px; background: #ccc; margin: 0 6px; }
  .social-dot { width: 20px; height: 20px; border-radius: 50%; background: var(--orange); }
  .main-nav { position: absolute; right: 236px; top: 85px; display: flex; gap: 22px; font-size: 14px; }
  .main-nav a { color: #555; text-decoration: none; }
  .main-nav a.active { color: var(--orange); }

  /* Hero */
  .hero { top: 126px; height: 414px; background: linear-gradient(100deg, #0a4b66 0%, #1a7f9d 45%, #0b5572 75%, #0a3a52 100%); color: var(--white); text-align: center; }
  .hero-art { position: absolute; inset: 0; }
  .hero-title { position: absolute; left: 0; right: 0; top: 176px; font-size: 29px; font-weight: 300; line-height: 1.15; }
  .hero-sub { position: absolute; left: 0; right: 0; top: 250px; font-size: 15px; font-weight: 300; }

  /* Reach */
  .reach { top: 540px; height: 546px; background: var(--dark); color: var(--white); }
  .section-title { text-align: center; font-weight: 400; font-size: 27px; }
  .reach .section-title { position: absolute; top: 32px; left: 0; right: 0; }
  .reach .tagline { position: absolute; top: 71px; left: 0; right: 0; text-align: center; font-size: 9px; color: var(--orange); }
  .world-map { position: absolute; left: 220px; top: 100px; width: 756px; height: 142px; background: linear-gradient(180deg, #eeebf3, #d5cfe1); }
  .icon-row { position: absolute; top: 282px; left: 330px; width: 520px; display: flex; align-items: center; justify-content: space-between; }
  .icon-row .rule { height: 3px; width: 108px; background: #555; }
  .features { position: absolute; top: 360px; left: 236px; display: flex; gap: 17px; }
  .feature { width: 232px; }
  .feature h3 { font-size: 19px; font-weight: 600; margin-bottom: 7px; }
  .feature p { font-size: 10px; line-height: 15.5px; color: #e5e5e5; }

  /* Device */
  .pitch { top: 1086px; height: 400px; background: var(--darker); overflow: hidden; }
  .device { position: absolute; left: 113px; top: 38px; width: 971px; height: 420px; background: #141414; border-radius: 22px; }
  .device-cam { position: absolute; left: 482px; top: 12px; width: 4px; height: 4px; border-radius: 50%; background: #3ac23a; }
  .device-screen { position: absolute; left: 39px; top: 40px; width: 893px; height: 380px; background: radial-gradient(ellipse at 50% 35%, #137a97 0%, #0b5a78 50%, #07374d 100%); color: var(--white); text-align: center; }
  .device-icons { position: absolute; top: 88px; left: 110px; width: 673px; display: flex; align-items: center; justify-content: space-between; }
  .device-icons .rule { width: 138px; height: 3px; background: var(--white); }
  .device-screen h2 { position: absolute; top: 190px; left: 0; right: 0; font-size: 27px; font-weight: 400; }
  .device-screen p { position: absolute; top: 240px; left: 0; right: 0; font-size: 11px; color: #8ec7d8; }

  /* Products */
  .products { top: 1486px; height: 440px; background: var(--mist); }
  .products .title-rule { position: absolute; top: 75px; height: 1px; width: 175px; background: #d2d2d2; }
  .products .section-title { position: absolute; top: 55px; left: 0; right: 0; color: #666; }
  .products .tagline { position: absolute; top: 96px; left: 0; right: 0; text-align: center; font-size: 10px; color: #666; }
  .product-list { position: absolute; top: 144px; left: 233px; display: flex; gap: 16px; }
  .product-card { width: 170px; }
  .product-frame { background: var(--white); padding: 7px; box-shadow: 2px 3px 6px rgba(0,0,0,.18); height: 162px; }
  .product-photo { width: 100%; height: 100%; }
  .product-name { margin-top: 17px; font-size: 14px; font-weight: 700; color: var(--orange); }
  .product-brand { font-size: 11px; color: #777; margin-top: 1px; }
  .pager { position: absolute; top: 382px; left: 0; right: 0; display: flex; justify-content: center; gap: 5px; }
  .pager span { width: 8px; height: 8px; border-radius: 50%; background: #999; }
  .pager span.on { background: var(--orange); }

  /* About */
  .about { top: 1926px; height: 276px; background: var(--white); text-align: center; }
  .about h2 { position: absolute; top: 40px; left: 0; right: 0; font-size: 23px; font-weight: 400; color: #222; }
  .about .lead { position: absolute; top: 80px; left: 275px; width: 650px; font-size: 11px; line-height: 17px; color: var(--orange); }
  .about .body { position: absolute; top: 121px; left: 272px; width: 656px; font-size: 10.5px; line-height: 17px; color: var(--muted); }
  .read-more { position: absolute; top: 212px; left: 0; right: 0; font-size: 12px; font-style: italic; font-weight: 600; color: #333; text-decoration: underline; }

  /* Footer */
  .site-footer { top: 2202px; height: 79px; background: var(--footer); border-top: 4px solid var(--teal); font-size: 12px; color: #ccc; }
  .footer-nav { position: absolute; left: 236px; top: 25px; display: flex; gap: 8px; }
  .footer-nav a { color: #ccc; text-decoration: none; }
  .footer-nav a.active { color: var(--orange); }
  .footer-nav .bar { color: #666; }
  .footer-meta { position: absolute; right: 236px; top: 26px; display: flex; gap: 14px; font-size: 10px; color: #888; align-items: center; }
  .footer-meta strong { color: var(--white); font-weight: 700; }
</style>
</head>
<body>

<header class="site-header">
  <div class="brand">
    <div class="brand-dot"></div>
    <div>
      <div class="brand-name">HDSG</div>
      <div class="brand-full">Harlow Digital Systems Group</div>
    </div>
  </div>
  <div class="contact-bar">
    <svg width="20" height="20" viewBox="0 0 24 24" aria-hidden="true"><path fill="#888" d="M6.6 10.8a15 15 0 0 0 6.6 6.6l2.2-2.2a1 1 0 0 1 1-.25 11 11 0 0 0 3.6.6 1 1 0 0 1 1 1V20a1 1 0 0 1-1 1A17 17 0 0 1 3 4a1 1 0 0 1 1-1h3.5a1 1 0 0 1 1 1 11 11 0 0 0 .6 3.6 1 1 0 0 1-.25 1z"/></svg>
    <span>+(065) 555 0142</span>
    <span class="sep"></span>
    <span class="social-dot"></span>
    <span class="social-dot"></span>
  </div>
  <nav class="main-nav">
    <a class="active" href="#">Home</a>
    <a href="#">About Us</a>
    <a href="#">Services</a>
    <a href="#">Products</a>
    <a href="#">Contact</a>
  </nav>
</header>

<section class="hero">
  <div class="hero-art" role="img" aria-label="Businessman in a suit standing before a large suspension bridge at dusk, tinted blue"></div>
  <h1 class="hero-title">HDSG change your IT life<br>supporting in time.</h1>
  <p class="hero-sub">Around the world. Around the clock.</p>
</section>

<section class="reach">
  <h2 class="section-title">Anywhere, anytime, where here to help.</h2>
  <p class="tagline">And we mean that.</p>
  <div class="world-map" role="img" aria-label="Folded paper world map with a location pin over Europe"></div>
  <div class="icon-row">
    <svg width="48" height="40" viewBox="0 0 48 40" aria-hidden="true"><g fill="#e8772a"><path d="M14 12 20 2h3l-6 10zM34 12 28 2h-3l6 10z"/><rect x="2" y="12" width="44" height="6" rx="1"/><path d="M6 20h36l-4 18H10z"/></g><g fill="#2d2d2d"><circle cx="16" cy="25" r="1.6"/><circle cx="24" cy="25" r="1.6"/><circle cx="32" cy="25" r="1.6"/><circle cx="20" cy="31" r="1.6"/><circle cx="28" cy="31" r="1.6"/></g></svg>
    <span class="rule"></span>
    <svg width="52" height="36" viewBox="0 0 52 36" aria-hidden="true"><g fill="#e8772a"><circle cx="14" cy="10" r="6"/><circle cx="38" cy="10" r="6"/><path d="M2 32c0-9 5-14 12-14s12 5 12 14zM26 32c0-9 5-14 12-14s12 5 12 14z"/><circle cx="26" cy="8" r="7" stroke="#2d2d2d" stroke-width="2"/><path d="M12 36c0-11 6-17 14-17s14 6 14 17z" stroke="#2d2d2d" stroke-width="2"/></g></svg>
    <span class="rule"></span>
    <svg width="30" height="44" viewBox="0 0 30 44" aria-hidden="true"><g fill="#e8772a"><path d="M15 2a13 13 0 0 1 8 23v5H7v-5a13 13 0 0 1 8-23z"/><rect x="8" y="32" width="14" height="3" rx="1"/><rect x="9" y="37" width="12" height="3" rx="1"/></g><path d="M11 12l4 10 4-10" stroke="#2d2d2d" stroke-width="2" fill="none"/></svg>
  </div>
  <div class="features">
    <div class="feature">
      <h3>Unque Products</h3>
      <p>Lorem ipsum dolor sit amet, consectetur adipisicing elit, sed do eiusmod tempor incididunt ut labore et dolore magna aliqua. Ut enim ad minim veniam, quis nostrud exercitation ullamco laboris nisi ut aliquip ex ea commodo consequat.</p>
    </div>
    <div class="feature">
      <h3>Win over the team</h3>
      <p>Lorem ipsum dolor sit amet, consectetur adipisicing elit, sed do eiusmod tempor incididunt ut labore et dolore magna aliqua. Ut enim ad minim veniam, quis nostrud exercitation ullamco laboris nisi ut aliquip ex ea commodo consequat.</p>
    </div>
    <div class="feature">
      <h3>After-sell commitment</h3>
      <p>Lorem ipsum dolor sit amet, consectetur adipisicing elit, sed do eiusmod tempor incididunt ut labore et dolore magna aliqua. Ut enim ad minim veniam, quis nostrud exercitation ullamco laboris nisi ut aliquip ex ea commodo consequat.</p>
    </div>
  </div>
</section>

<section class="pitch">
  <div class="device">
    <span class="device-cam"></span>
    <div class="device-screen">
      <div class="device-icons">
        <svg width="68" height="58" viewBox="0 0 48 40" aria-hidden="true"><g fill="#fff"><path d="M14 12 20 2h3l-6 10zM34 12 28 2h-3l6 10z"/><rect x="2" y="12" width="44" height="6" rx="1"/><path d="M6 20h36l-4 18H10z"/></g><g fill="#0b5a78"><circle cx="16" cy="25" r="1.6"/><circle cx="24" cy="25" r="1.6"/><circle cx="32" cy="25" r="1.6"/><circle cx="20" cy="31" r="1.6"/><circle cx="28" cy="31" r="1.6"/></g></svg>
        <span class="rule"></span>
        <svg width="80" height="56" viewBox="0 0 52 36" aria-hidden="true"><g fill="#fff"><circle cx="14" cy="10" r="6"/><circle cx="38" cy="10" r="6"/><path d="M2 32c0-9 5-14 12-14s12 5 12 14zM26 32c0-9 5-14 12-14s12 5 12 14z"/><circle cx="26" cy="8" r="7" stroke="#0c5e7c" stroke-width="2"/><path d="M12 36c0-11 6-17 14-17s14 6 14 17z" stroke="#0c5e7c" stroke-width="2"/></g></svg>
        <span class="rule"></span>
        <svg width="40" height="60" viewBox="0 0 30 44" aria-hidden="true"><g fill="#fff"><path d="M15 2a13 13 0 0 1 8 23v5H7v-5a13 13 0 0 1 8-23z"/><rect x="8" y="32" width="14" height="3" rx="1"/><rect x="9" y="37" width="12" height="3" rx="1"/></g><path d="M11 12l4 10 4-10" stroke="#0c5e7c" stroke-width="2" fill="none"/></svg>
      </div>
      <h2>A simple call lead to big solution</h2>
      <p>We started small but grew quickly.</p>
    </div>
  </div>
</section>

<section class="products">
  <span class="title-rule" style="left:236px"></span>
  <span class="title-rule" style="right:236px"></span>
  <h2 class="section-title">Trend based IT Products</h2>
  <p class="tagline">Some of our unique items.</p>
  <div class="product-list">
    <article class="product-card">
      <div class="product-frame"><div class="product-photo" role="img" aria-label="Open laptop on a desk" style="background:linear-gradient(160deg,#6f8aa3,#1c2a3a)"></div></div>
      <div class="product-name">Product Name</div>
      <div class="product-brand">Brand Name</div>
    </article>
    <article class="product-card">
      <div class="product-frame"><div class="product-photo" role="img" aria-label="Tablet lying on a dark surface" style="background:linear-gradient(160deg,#5a5a5a,#1e1e1e)"></div></div>
      <div class="product-name">Product Name</div>
      <div class="product-brand">Brand Name</div>
    </article>
    <article class="product-card">
      <div class="product-frame"><div class="product-photo" role="img" aria-label="Tablet with detachable keyboard" style="background:linear-gradient(160deg,#4b4b4b,#141414)"></div></div>
      <div class="product-name">Product Name</div>
      <div class="product-brand">Brand Name</div>
    </article>
    <article class="product-card">
      <div class="product-frame"><div class="product-photo" role="img" aria-label="Smartphones stacked on a table" style="background:linear-gradient(160deg,#d0d0d0,#2a2a2a)"></div></div>
      <div class="product-name">Product Name</div>
      <div class="product-brand">Brand Name</div>
    </article>
  </div>
  <div class="pager"><span class="on"></span><span></span><span></span><span></span></div>
</section>

<section class="about">
  <h2>Know about us</h2>
  <p class="lead">Lorem ipsum dolor sit amet, consectetur adipiscing elit. Donec eu turpis purus. Pellentesque ullamcorper mauris vitae sapien bibendum tincidunt. Check out here.</p>
  <p class="body">Morbi malesuada mauris sed nibh placerat sit amet posuere libero egestas. Vestibulum consectetur iaculis est, at dapibus purus malesuada vitae. Mauris sollicitudin aliquam scelerisque. Vestibulum ante ipsum primis in faucibus orci luctus et ultrices posuere cubilia Curae; Donec et mi sem. Duis tristique elementum tristique. Sed ac magna quis erat sagittis suscipit. Phasellus faucibus rhoncus massa, non laoreet lorem fringilla non.</p>
  <a class="read-more" href="#">Read more &gt;&gt;</a>
</section>

<footer class="site-footer">
  <nav class="footer-nav">
    <a class="active" href="#">Home</a><span class="bar">|</span>
    <a href="#">About Us</a><span class="bar">|</span>
    <a href="#">Services</a><span class="bar">|</span>
    <a href="#">Products</a><span class="bar">|</span>
    <a href="#">Contact</a>
  </nav>
  <div class="footer-meta">
    <span>Copyright@2014, HDSG. All rights are reserved.</span>
    <span>|</span>
    <strong>Chatter</strong>
    <strong>Friendwall</strong>
  </div>
</footer>

</body>
</html>
```